Harwick Physiotherapy needs a brochure that will highlight and sell our services to prospective clie

Harwick Physiotherapy. The treatment you need , the care you deserve.

We need a brochure design for our musculoskeletal physiotherapy business. It needs to sell our service to prospective clients and to referrers and communicate our values and mission. It needs to incorporate our services of: back and neck pain, muscle and joint sprains and strains, sports injury management, including video assessment, acupuncture, Pilates, women's health/pelvic floor physio, deep tissue massage. We use technology including video analysis to improve patient outcomes. Our website is http://harwickphysio.co.nz attached are some images from web site and some graphics including our logo

Ideally a front page with our logo and graphics and bulletin points of our services

Sports Injuries
Back , neck and joint pain
Orthopedic rehabilitation
Acupuncture
Pelvic floor Physiotherapy

Then inside our USP's why us (see our web site) plus ....
We provide expert diagnosis of your problem and committed/dedicated to providing the best possible solution to get you back to what you love and improve your performance
Also we specialise in the use of technology with video analysis (http://www.strivelens.com/), digital postural analysis software (http://alignmetrix.com/mobile/), computer graphics for education (http://applications.anatovista.com/shoulder_pro) and video/online exercise programs (https://www.kinetrova.org/index.php), online booking (http://nzappts.bookrally.com/harwick/)
Long appointments , not rushed , to give us time to help

Then sections for:

Physiotherapy
sports physio
Orthopaedic rehab
back and neck pain
acupuncture
women's health inside
take info from our website, but also I can upload brochures from Rehab Guild NZ, take the best out of each of those and combine with our web info to provide description for each.

And on back all contact detail and QR code for our website

Target Market(s)

mostly 40 to 60 comfortably off, educated, active, some sporty, healthy, middle class

Industry/Entity Type

Education

Requirements
Must have
• Must match our website with the logo and pictures on home page
brochure to be A4 trifold DLE, please match our font or use one we can use easily
Nice to have
• not too busy, give our customers good reasons to use our services,

```html
<!DOCTYPE html>
<html lang="en">
<head>
<meta charset="utf-8">
<title>Harwick Physiotherapy – Inside Panels</title>
<link href="https://fonts.googleapis.com/css2?family=Barlow:wght@400;500;600;700&display=swap" rel="stylesheet">
<style>
  :root {
    --lime: #c9dc1e;
    --paper: #efedea;
    --paper-dark: #e4e1dc;
    --ink: #1b1b1b;
    --body: #555352;
    --orange: #f27a1c;
    --bar-grey: #9a9896;
    --cyan: #22b4e2;
    --frame: #ffffff;
    --bg: #d9d7d4;
  }
  * { box-sizing: border-box; margin: 0; padding: 0; }
  html, body { width: 1200px; height: 1107px; overflow: hidden; background: var(--bg); }
  body { font-family: "Barlow", Arial, sans-serif; }

  .brochure { position: relative; width: 1200px; height: 1107px; display: flex; overflow: hidden; }
  .panel { position: relative; width: 400px; height: 1107px; padding: 0 30px 0 34px; }
  .panel--why { background: var(--lime); color: var(--ink); }
  .panel--services, .panel--movement {
    background: linear-gradient(180deg, var(--paper) 0%, var(--paper-dark) 100%);
    color: var(--body);
  }
  .panel--services { box-shadow: inset 8px 0 14px -8px rgba(0,0,0,.25); }
  .panel--movement { box-shadow: inset 8px 0 14px -8px rgba(0,0,0,.18); }

  .panel-rule { position: absolute; left: 0; top: 0; width: 400px; height: 140px; }

  .panel-title { position: relative; font-weight: 600; line-height: 1; }
  .panel--why .panel-title { font-size: 32px; color: var(--ink); padding-top: 34px; }
  .panel--services .panel-title { font-size: 30px; color: var(--orange); padding-top: 90px; padding-left: 22px; }
  .panel--movement .panel-title { font-size: 30px; color: var(--orange); padding-top: 44px; }

  .section-head { font-weight: 700; margin-top: 14px; margin-bottom: 3px; line-height: 1.2; }
  .panel--why .section-head { font-size: 17px; color: var(--ink); }
  .panel--why .section-head:first-of-type { margin-top: 44px; }
  .panel--services .section-head,
  .panel--movement .section-head { font-size: 19px; font-weight: 500; color: var(--orange); margin-top: 18px; }
  .panel--services .section-head:first-of-type { margin-top: 50px; }
  .panel--movement .section-head:first-of-type { margin-top: 66px; }

  .copy { font-size: 14.5px; line-height: 1.3; }
  .panel--why .copy { font-size: 14.5px; line-height: 1.26; }

  .tagline { text-align: center; color: #fff; font-size: 21px; font-weight: 500; line-height: 1.2; margin-top: 12px; }

  .checklist { list-style: none; margin-top: 4px; font-size: 14.5px; line-height: 1.3; }
  .checklist li { position: relative; padding-left: 20px; margin-bottom: 3px; }
  .checklist li::before { content: ""; position: absolute; left: 4px; top: 7px; width: 6px; height: 6px; border-radius: 50%; background: var(--body); }
  .lead-in { margin-top: 14px; font-size: 14.5px; }

  .cyan-band { position: absolute; left: 0; bottom: 0; width: 1200px; height: 95px; background: var(--cyan); }

  .photo {
    position: absolute; border: 9px solid var(--frame);
    box-shadow: 0 6px 14px rgba(0,0,0,.3);
  }
  .photo--back-treatment { left: -12px; top: 808px; width: 200px; height: 220px; transform: rotate(-3deg);
    background: linear-gradient(160deg, #d8b8a4 0%, #8c6a5a 45%, #2a2220 100%); }
  .photo--knee-runner { left: 176px; top: 822px; width: 230px; height: 245px; transform: rotate(4deg);
    background: linear-gradient(180deg, #9fc4e6 0%, #c9d9e6 45%, #7f7f7f 75%, #3b3b3b 100%); }
  .photo--acupuncture { left: 420px; top: 800px; width: 240px; height: 232px; transform: rotate(-2deg);
    background: linear-gradient(200deg, #e9c9b0 0%, #c89a82 40%, #1f2a4c 75%, #141c38 100%); }
  .photo--knee-assessment { left: 652px; top: 814px; width: 228px; height: 255px; transform: rotate(4deg);
    background: linear-gradient(160deg, #cfe3f3 0%, #e2c2a8 45%, #b48a70 70%, #2d2d2d 100%); }
  .photo--pilates { left: 880px; top: 862px; width: 190px; height: 200px; transform: rotate(-3deg);
    background: linear-gradient(180deg, #efe9e1 0%, #e3d6c6 50%, #a8a6a6 80%, #5aa9c8 100%); }
  .photo--facial-massage { left: 1052px; top: 824px; width: 170px; height: 205px; transform: rotate(2deg);
    background: linear-gradient(150deg, #f4ece6 0%, #e7c6ae 45%, #caa186 75%, #f6f2ee 100%); }
</style>
</head>
<body>
<main class="brochure">

  <section class="panel panel--why">
    <svg class="panel-rule" viewBox="0 0 400 140" aria-hidden="true">
      <rect x="0" y="82" width="290" height="9" fill="#1b1b1b"/>
      <circle cx="292" cy="86" r="11" fill="#1b1b1b"/>
    </svg>
    <h2 class="panel-title">Why Us</h2>

    <h3 class="section-head">The Harwick Physiotherapy Difference</h3>
    <p class="copy">Our highly trained, experienced, professional Physiotherapists are committed to giving you the best outcomes to resolve your problem. We are experts at injury diagnosis. We are qualified to post graduate level and have over thirty years of clinical experience working in private practice between us. We care about you and your health and are absolutely dedicated to providing you with the best possible service. For more about our services read on</p>

    <h3 class="section-head">What Do We Treat?</h3>
    <p class="copy">If it's musculo-skeletal issue, then we deal with it. Yes we see a lot of sports injuries, but we are not just for sports people. We specialise in every day problems in every day people. Back and neck pain, joint sprains, muscle strain, arthritis, head aches, falls, incontinence. For a list of some of the conditions we treat, and some further information and free advice.</p>

    <h3 class="section-head">Our Guarantee</h3>
    <p class="copy">We guarantee that we will provide a professional service, to your satisfaction. We pride ourselves on the delivery of the highest quality physiotherapy, massage, acupuncture and rehabilitation services. Our philosophy is that</p>
    <p class="tagline">If YOU are not happy then<br>WE are not happy.</p>
  </section>

  <section class="panel panel--services">
    <svg class="panel-rule" viewBox="0 0 400 140" aria-hidden="true">
      <path d="M12 112 Q12 78 44 78 L400 78" fill="none" stroke="#9a9896" stroke-width="9"/>
      <circle cx="12" cy="114" r="7" fill="#9a9896"/>
    </svg>
    <h2 class="panel-title">Our Services</h2>

    <h3 class="section-head">Physiotherapy</h3>
    <p class="copy">Physiotherapy is a health care profession primarily concerned with the remediation of impairments and disabilities and the promotion of mobility, functional ability, quality of life and movement potential through examination, evaluation, diagnosis and physical intervention. All of our therapists have over ten years of experience in managing musculo-skeletal conditions.</p>

    <h3 class="section-head">Sports physio</h3>
    <p class="copy">The most common sporting injuries (according to ICA) are to the head, shoulders, hamstrings, knees and ankles. Most sports injuries are easily preventable, which is where a physio comes in. They can help you rehabilitate from an injury, show you how to prevent one occurring or work with you to improve your sporting performance.</p>

    <h3 class="section-head">Orthotic Prescription</h3>
    <p class="copy">We stock Stridefit. These are heat molded to customise to your feet. They are proven to be effective for the management of lower back pain, hip pain, knee problems as well as Achilles injuries, plantar fasciitis, and other painful foot conditions.</p>
  </section>

  <section class="panel panel--movement">
    <svg class="panel-rule" viewBox="0 0 400 140" aria-hidden="true">
      <path d="M0 112 L22 112 Q40 112 60 104 L400 86" fill="none" stroke="#9a9896" stroke-width="9"/>
    </svg>
    <h2 class="panel-title">Movement for life</h2>

    <h3 class="section-head">Back and neck pain</h3>
    <p class="copy">Back and neck pain text not found on your webite kindly provide me the text regarding Back and neck pain. I am trying to design this trifold brochure as per your requirement but i didn't found the text regarding back and neck pain kindly provide me the text so i can replace it easily. thank you</p>

    <h3 class="section-head">Women's Health and pelvic floor physiotherapy</h3>
    <p class="copy">Pregnancy, menopause, gynecological procedures and a history of back pain or pelvic pain can all lead to either pelvic floor weakness or dysfunction. Other risk factors include being overweight, a chronic cough or sneeze along with repeat heavy lifting. Click here to see our free pelvic Floor screening test that will help you figure out if you are at risk of pelvic floor problems.</p>

    <h3 class="section-head">Deep Tissue and Sports Massage</h3>
    <p class="copy">For injury prevention and treatment or just for relaxation, call us and ask for details</p>

    <p class="lead-in">Are you:</p>
    <ul class="checklist">
      <li>Recovering from an injury?</li>
      <li>Wanting to prevent an injury recurring?</li>
      <li>Or just looking for a form of exercise to correct posture, strengthen, tone and stretch your body</li>
    </ul>
  </section>

  <div class="cyan-band"></div>

  <div class="photo photo--back-treatment" role="img" aria-label="Physiotherapist treating a patient's lower back"></div>
  <div class="photo photo--knee-runner" role="img" aria-label="Runner holding an injured knee outdoors"></div>
  <div class="photo photo--acupuncture" role="img" aria-label="Acupuncture needles in a patient's leg"></div>
  <div class="photo photo--knee-assessment" role="img" aria-label="Therapist assessing a patient's knee"></div>
  <div class="photo photo--pilates" role="img" aria-label="Woman doing a Pilates exercise on a mat"></div>
  <div class="photo photo--facial-massage" role="img" aria-label="Relaxing head and face massage"></div>

</main>
</body>
</html>
```